Commercial HVAC and Refrigeration Business cards

Frost-Haven Company is looking for flashy new business cards! We design, install, service and maintain commercial refrigeration, air conditioning, heating and refrigeration equipment. Our colors are blue and white. I'm open to single and double sided designs. Each employee will have their own business card. I've attached a copy of our current logo.

Our website, office and cell phone (cell phone is optional), email address should be clearly legible. "24 Hour Service" and the services we offer are; Sales, Service, Design, Installation, Maintenance. Refrigeration, Heating, Air Conditioning, Ice Machines. Does not have to be in any order.

Target Market(s)

Commercial; Restaurants, hotels, bars, breweries etc.

Industry/Entity Type

Hvac

Contact Information for Business Card

Name; Job Title, Phone Number, Email Address. www.frost-haven-example.com 24 Hour Service. We provide - Sales, Design, Installation, Service, Maintenance. We service - Refrigeration, Heating, Air Conditioning, Ice Machines

Font styles to use
Other font styles liked:
• Be creative

Colors
0255a3
ffffff

Requirements
Must have
• Professional appearance and appeal to commercial clients in the food-service and hospitality industry. Must be clearly legible and easy to understand.
Nice to have
• We want to sell maintenance agreements, perhaps we can use the back of the card to tie into a webpage about our maintenance agreements.
Should not have
• Cartoons or unprofessional. Nothing too edgy.

```html
<!DOCTYPE html>
<html lang="en">
<head>
<meta charset="utf-8">
<title>Frost-Haven Company – Business Cards</title>
<link rel="stylesheet" href="https://fonts.googleapis.com/css2?family=PT+Sans:wght@400;700&display=swap">
<style>
  :root {
    --brand-blue: #2a4aa6;
    --brand-blue-deep: #0255a3;
    --card-white: #ffffff;
    --stage: #eceef2;
    --shadow: rgba(20, 30, 60, 0.18);
  }
  * { box-sizing: border-box; margin: 0; padding: 0; }
  html, body { width: 1200px; height: 780px; overflow: hidden; }
  body {
    background: var(--stage);
    font-family: "PT Sans", "Segoe UI", sans-serif;
    color: var(--brand-blue);
    position: relative;
  }
  .card {
    position: absolute;
    width: 540px;
    height: 309px;
    background: var(--card-white);
    box-shadow: 0 6px 22px var(--shadow);
    overflow: hidden;
  }
  .card--front { left: 40px; top: 235px; }
  .card--back  { left: 620px; top: 235px; }

  /* Front */
  .front__body { position: absolute; left: 34px; top: 26px; right: 30px; }
  .front__company { font-size: 34px; font-weight: 400; letter-spacing: 0.2px; }
  .front__person { margin-top: 30px; }
  .front__name { font-size: 21px; font-weight: 700; line-height: 1.1; }
  .front__title { font-size: 14px; line-height: 1.2; }
  .front__contacts { list-style: none; margin-top: 10px; font-size: 14px; line-height: 1.35; }
  .front__contacts li { display: flex; align-items: center; gap: 8px; }
  .front__contacts svg { width: 13px; height: 13px; flex: none; }
  .front__band {
    position: absolute; left: 0; right: 0; bottom: 0; height: 86px;
    background: var(--brand-blue);
    display: flex; align-items: center; justify-content: center;
  }
  .front__band-name { color: var(--card-white); font-size: 30px; font-weight: 700; letter-spacing: 0.5px; }

  /* Back */
  .back__brand {
    position: absolute; top: 34px; left: 0; right: 0; text-align: center;
    font-size: 38px; font-weight: 700; color: var(--brand-blue);
  }
  .back__offer-title {
    position: absolute; top: 108px; left: 0; right: 0; text-align: center;
    font-size: 17px; letter-spacing: 0.5px;
  }
  .back__services {
    position: absolute; top: 140px; left: 0; right: 0; text-align: center;
    font-size: 14.5px; line-height: 1.55;
  }
  .back__band {
    position: absolute; left: 0; right: 0; bottom: 0; height: 56px;
    background: var(--brand-blue);
    display: flex; align-items: center; justify-content: center;
    color: var(--card-white); font-size: 19px; letter-spacing: 0.4px;
  }
</style>
</head>
<body>

<section class="card card--front" aria-label="Business card front">
  <div class="front__body">
    <h1 class="front__company">Frost-Haven Company</h1>
    <div class="front__person">
      <p class="front__name">Employee Name</p>
      <p class="front__title">Director</p>
    </div>
    <ul class="front__contacts">
      <li>
        <svg viewBox="0 0 13 13" aria-hidden="true"><rect width="13" height="13" fill="#2a4aa6"/><path d="M4 3h1.6l.7 1.8-1 .7a5 5 0 0 0 2.2 2.2l.7-1 1.8.7V10A6.5 6.5 0 0 1 3 4z" fill="#fff"/></svg>
        000-000-0000
      </li>
      <li>
        <svg viewBox="0 0 13 13" aria-hidden="true"><rect width="13" height="13" fill="#2a4aa6"/><rect x="2.5" y="4" width="8" height="5.5" fill="none" stroke="#fff" stroke-width="1"/><path d="M2.5 4l4 3 4-3" fill="none" stroke="#fff" stroke-width="1"/></svg>
        your@mail-example.com
      </li>
      <li>
        <svg viewBox="0 0 13 13" aria-hidden="true"><rect width="13" height="13" fill="#2a4aa6"/><circle cx="6.5" cy="6.5" r="4" fill="none" stroke="#fff" stroke-width="1"/><ellipse cx="6.5" cy="6.5" rx="1.8" ry="4" fill="none" stroke="#fff" stroke-width="0.8"/><path d="M2.5 6.5h8" stroke="#fff" stroke-width="0.8"/></svg>
        www.frost-haven-example.com
      </li>
    </ul>
  </div>
  <div class="front__band">
    <span class="front__band-name">Frost-Haven Company</span>
  </div>
</section>

<section class="card card--back" aria-label="Business card back">
  <p class="back__brand">Frost-Haven Company</p>
  <p class="back__offer-title">WE OFFER ARE</p>
  <p class="back__services">
    Sales | Service | Design | Installation | Maintenance | Refrigeration | Heating<br>
    Air Conditioning | Ice Machines
  </p>
  <div class="back__band">24 Hour Service</div>
</section>

</body>
</html>
```